Producer Needs a Movie Poster for a Dramatic Film

We need a movie poster for a new dramatic film called "Past the Lantern".
Synopisis: A young drug addict (cocaine and alcohol), ROSS PENDRY, has hit rock bottom after a continuous downward spiral of alcoholism and drug abuse, leaving him with nothing to live for. His ex-girlfriend left him. His best friend doesn’t want anything to do with him. Unable to rehabilitate himself after multiple attempts, he attempts suicide (Jumping off of a high-rise apartment building).
We want the poster to give the dark feel of the film. It should be serious and personable.
We want the three lead actors to be listed on the top of the poster from left to right (Gregory Lint, Miriam Kessub, Osric Demmelby).
The title of the film, Past the Lantern, should be in the center of the poster.
We want "Coming Soon" centered on the bottom of the poster.

No pictures will be provided for this poster, so be creative and make something special for us to use. We're looking for a variety of good ideas.

We're excited to see what you come up with!

Please, make sure you provide us with files we can easily use. Also, we would like a copy of the film title in a separate file for easy use as well. So, two files total (One with the poster, One with just the film title by itself).

Industry/Entity Type

Movie

Requirements
Must have
• We want the three lead actors to be listed on the top of the poster from left to right (Gregory Lint, Miriam Kessub, Osric Demmelby).
• The title of the film, Past the Lantern, should be in the center of the poster.
• We want "Coming Soon" centered on the bottom of the poster.
• Please, make sure you provide us with files we can easily use. Also, we would like a copy of the film title in a separate file for easy use as well. So, two files total (One with the poster, One with just the film title by itself).
Should not have
• Should not have a person on the poster unless they are unrecognizable and you can't see any characteristics. We can't have someone on the poster who won't be in the movie.
• Don't put each locations that won't be in the film either. It takes place in LOs Angeles. Mostly on a high-rise apartment building rooftop.

```html
<!DOCTYPE html>
<html lang="en">
<head>
<meta charset="utf-8">
<title>Past the Lantern – Poster</title>
<link href="https://fonts.googleapis.com/css2?family=Bebas+Neue&display=swap" rel="stylesheet">
<style>
  :root {
    --backdrop: #e6e7e9;
    --paper: #ffffff;
    --plum: #7b2249;
    --plum-deep: #2a1430;
    --amber: #d89a45;
    --night: #3a2236;
    --rule: #8e8e8e;
  }
  * { margin: 0; padding: 0; box-sizing: border-box; }
  html, body {
    width: 900px; height: 1200px; overflow: hidden;
    background: var(--backdrop);
  }
  .canvas { position: relative; width: 900px; height: 1200px; }
  .poster {
    position: absolute; left: 147px; top: 171px;
    width: 606px; height: 857px;
    background: var(--paper); overflow: hidden;
    font-family: "Bebas Neue", "Arial Narrow", sans-serif;
    color: var(--plum);
  }
  .speed-lines { position: absolute; inset: 0; }
  .speed-lines line { stroke: var(--rule); stroke-width: 0.8; }

  .cast {
    position: absolute; left: 168px; top: 172px;
    transform: rotate(-12deg); transform-origin: left top;
    list-style: none; font-size: 19px; line-height: 19px; letter-spacing: 0.3px;
  }
  .cast li:nth-child(2) { padding-left: 20px; }
  .cast li:nth-child(3) { padding-left: 6px; }

  .title {
    position: absolute; left: 88px; top: 268px;
    transform: rotate(-10deg); transform-origin: left top;
    line-height: 0.82;
  }
  .title-lead {
    display: block; padding-left: 150px;
    font-size: 116px; letter-spacing: 1px;
    background: linear-gradient(180deg, var(--plum) 55%, var(--night) 100%);
    -webkit-background-clip: text; background-clip: text; color: transparent;
  }
  .title-main {
    display: block; font-size: 168px; letter-spacing: -1px;
    background: linear-gradient(170deg, var(--amber) 0%, #8a4a52 30%, var(--night) 60%, var(--plum-deep) 100%);
    -webkit-background-clip: text; background-clip: text; color: transparent;
  }

  .release {
    position: absolute; left: 402px; top: 752px;
    transform: rotate(-11deg); transform-origin: left top;
    font-size: 25px; letter-spacing: 0.3px;
  }
</style>
</head>
<body>
<div class="canvas">
  <main class="poster">
    <svg class="speed-lines" width="606" height="857" viewBox="147 171 606 857" aria-hidden="true">
      <line x1="245" y1="251" x2="400" y2="203"/>
      <line x1="585" y1="264" x2="738" y2="216"/>
      <line x1="305" y1="395" x2="458" y2="347"/>
      <line x1="183" y1="447" x2="565" y2="348"/>
      <line x1="232" y1="437" x2="430" y2="382"/>
      <line x1="272" y1="493" x2="697" y2="400"/>
      <line x1="160" y1="713" x2="755" y2="570"/>
      <line x1="548" y1="735" x2="700" y2="688"/>
      <line x1="352" y1="888" x2="505" y2="840"/>
      <line x1="607" y1="888" x2="752" y2="843"/>
      <line x1="147" y1="1008" x2="278" y2="967"/>
      <line x1="471" y1="997" x2="752" y2="925"/>
      <line x1="525" y1="1028" x2="610" y2="1002"/>
      <line x1="645" y1="997" x2="752" y2="965"/>
    </svg>

    <ul class="cast">
      <li>Gregory Lint</li>
      <li>Miriam Kessub</li>
      <li>Osric Demmelby</li>
    </ul>

    <h1 class="title">
      <span class="title-lead">Past the</span>
      <span class="title-main" role="img" aria-label="Lantern – lettering filled with a night view of city lights and a lone figure on a rooftop">Lantern</span>
    </h1>

    <p class="release">Coming Soon</p>
  </main>
</div>
</body>
</html>
```